WardPivot landing page

The existing website at www.wardpivot-example.com needs updating. I've attached some marketing material for the color scheme to be used and potential content. The tagline should be "Real-Time Operational Intelligence." I want the landing page to be in 3 categories in this order and features within each category. Plenty of images are preferred and wording can be modified.
Wardpivot Command Centre
- Live Incident tracking and reporting with escalation on critical incidents if necessary
- Geofence Monitoring to ensure guards at the right location at the right time.
- Smart scheduling to ensure the correct training and certifications are assigned to the appropriate guard required.
- Camera compatibility to capture live and historical video for incident reporting
WardPivot Back Office Administration
- Automate Police report filing using data from submitted incidents when required.
- Track all required KPIs on a per site basis such as vehicle inspections, patrol tour details, etc
- Payroll and Invoicing using smart shift reports
- Create and manage client sites with configurable geofencing
WardPivot App
- Guard can see all site details and instructions when logging onto shift
- Ability to view all incidents that have occured at that particular site over the last 'x' days. Understand what has been happening and when.
- Report incidents with all relevant information including photo and video
- Recieve alerts when repeat offences are occuring within a configurable vicinity.

Target Market(s)

Retailers and guard companies

Coding

Coded - Design and coding required

Number of Pages Required

1 page

Requirements
Nice to have
• Use the look and feel of the logo in the design

```html
<!DOCTYPE html>
<html lang="en">
<head>
<meta charset="utf-8">
<title>WardPivot – Real-Time Operational Intelligence</title>
<link rel="stylesheet" href="https://fonts.googleapis.com/css2?family=Poppins:wght@400;500;600&family=Red+Hat+Display:wght@600;700;800&display=swap">
<style>
:root{
  --navy:#0c2a4d;
  --navy-deep:#081d38;
  --blue:#1a8ad4;
  --blue-bright:#2196e8;
  --sky:#e0f2fc;
  --text:#1e2a3a;
  --white:#ffffff;
  --field:#f7f9fb;
}
*{box-sizing:border-box;margin:0;padding:0}
html,body{width:1200px;height:4988px;overflow:hidden}
body{position:relative;background:var(--white);font-family:"Poppins",sans-serif;color:var(--text)}
.abs{position:absolute}
.heading{font-family:"Red Hat Display",sans-serif;font-weight:700;color:var(--navy)}
.accent{color:var(--blue)}

/* header */
.site-header{left:0;top:0;width:1200px;height:140px;z-index:5}
.brand{left:65px;top:40px;display:flex;align-items:center;gap:10px}
.brand-dot{width:22px;height:22px;border-radius:50%;background:var(--blue)}
.brand-name{font-family:"Red Hat Display",sans-serif;font-weight:700;font-size:26px;color:var(--navy)}
.nav{left:425px;top:64px;display:flex;align-items:center;font-size:13px;color:var(--navy)}
.nav a{text-decoration:none;color:inherit;margin-right:40px;padding-bottom:8px}
.nav a.active{color:var(--blue);border-bottom:2px solid var(--blue)}
.btn{display:inline-flex;align-items:center;justify-content:center;border-radius:20px;font-size:13px;font-weight:600;color:var(--white);text-decoration:none}
.btn-demo{left:858px;top:62px;width:154px;height:36px;background:var(--navy)}
.btn-login{left:1020px;top:62px;width:114px;height:36px;background:var(--blue-bright);gap:6px}

/* hero */
.hero-bg{left:0;top:0}
.hero-title{left:0;top:360px;width:1200px;text-align:center;font-family:"Red Hat Display",sans-serif;font-weight:700;font-size:124px;color:var(--white);line-height:1}
.hero-tagline{left:0;top:498px;width:1200px;text-align:center;font-family:"Red Hat Display",sans-serif;font-weight:700;font-size:56px;line-height:68px;color:var(--white);text-transform:uppercase}
.hero-list{list-style:none;font-family:"Red Hat Display",sans-serif;font-weight:600;font-size:25px;color:var(--white)}
.hero-list li{display:flex;align-items:center;gap:20px;height:49px}
.hero-list.col-a{left:200px;top:657px}
.hero-list.col-b{left:604px;top:657px}

.tick{flex:none;width:20px;height:20px}

/* features */
.section-mark{width:40px;height:40px;border-radius:50%;background:var(--blue);border:6px solid var(--navy)}
.section-title{font-size:60px;text-align:center;width:1200px;left:0}
.blob{border-radius:50%;background:var(--sky)}
.feature-title{font-size:42px;line-height:44px}
.feature-list{list-style:none;font-size:14.5px;line-height:24px;color:var(--text)}
.feature-list li{display:flex;gap:10px;margin-bottom:3px}
.feature-list .tick{width:16px;height:16px;margin-top:4px}

/* cta */
.cta-title{left:0;top:3228px;width:1200px;text-align:center;font-size:66px;line-height:78px;color:var(--white)}
.btn-cta{left:426px;top:3425px;width:348px;height:60px;border-radius:30px;background:var(--blue-bright);font-family:"Red Hat Display",sans-serif;font-size:23px;font-weight:700;gap:16px;letter-spacing:.5px}

/* contact */
.contact-title{left:586px;top:3782px;width:418px;text-align:center;font-size:54px}
.field{background:var(--white);border:1px solid #e3e8ee;box-shadow:0 2px 8px rgba(12,42,77,.12);font-size:10px;color:#9aa4ae;padding:12px 18px}
.btn-submit{left:710px;top:4176px;width:170px;height:58px;border-radius:29px;background:var(--navy);font-size:19px;gap:14px}

/* footer */
.footer-name{left:0;top:4655px;width:1200px;text-align:center;font-family:"Red Hat Display",sans-serif;font-weight:700;font-size:54px;color:var(--white)}
.footer-mark{left:572px;top:4555px;width:56px;height:56px;border-radius:50%;background:var(--blue)}
.contact-item{display:flex;align-items:center;gap:14px;color:var(--white);font-size:13px;line-height:19px}
.contact-icon{width:32px;height:32px;border-radius:6px;background:var(--blue-bright);display:flex;align-items:center;justify-content:center}
.footer-rule{left:70px;top:4843px;width:1064px;height:1px;background:rgba(255,255,255,.35)}
.footer-links{left:0;top:4868px;width:1200px;font-size:12.5px;font-weight:500;color:var(--white)}
.footer-links span{position:absolute;transform:translateX(-50%);white-space:nowrap}
.footer-bar{left:0;top:4925px;width:1200px;height:63px;background:var(--navy-deep)}
.copyright{left:70px;top:4950px;font-size:11.5px;color:var(--white)}
.social{top:4945px;width:24px;height:24px;background:var(--blue-bright);border-radius:3px}
</style>
</head>
<body>

<!-- hero background -->
<svg class="abs hero-bg" width="1200" height="1010" role="img" aria-label="Photo of a security analyst in front of glowing data dashboards">
  <defs>
    <linearGradient id="heroGrad" x1="0" y1="0" x2="1" y2="1">
      <stop offset="0" stop-color="#1d4a78"/>
      <stop offset=".5" stop-color="#123560"/>
      <stop offset="1" stop-color="#0a2142"/>
    </linearGradient>
  </defs>
  <path d="M0 190 Q600 110 1200 190 L1200 755 Q880 860 600 1004 Q320 860 0 755 Z" fill="url(#heroGrad)"/>
</svg>

<header class="abs site-header">
  <div class="abs brand"><span class="brand-dot"></span><span class="brand-name">WardPivot</span></div>
  <nav class="abs nav">
    <a class="active" href="#">HOME</a>
    <a href="#">FEATURES ▾</a>
    <a href="#">PRICING</a>
    <a href="#">CONTACT US</a>
  </nav>
  <a class="abs btn btn-demo" href="#">REQUEST DEMO</a>
  <a class="abs btn btn-login" href="#">
    <svg width="12" height="12" viewBox="0 0 12 12"><circle cx="6" cy="3.5" r="3" fill="#fff"/><path d="M0 12 Q6 4 12 12Z" fill="#fff"/></svg>LOGIN</a>
</header>

<h1 class="abs hero-title">WardPivot</h1>
<p class="abs hero-tagline">Real-Time Operational<br>Intelligence</p>
<ul class="abs hero-list col-a">
  <li><svg class="tick" viewBox="0 0 20 20"><circle cx="10" cy="10" r="10" fill="#2196e8"/><path d="M5.5 10.5l3 3 6-6.5" stroke="#fff" stroke-width="2.2" fill="none"/></svg>Geofence Monitoring</li>
  <li><svg class="tick" viewBox="0 0 20 20"><circle cx="10" cy="10" r="10" fill="#2196e8"/><path d="M5.5 10.5l3 3 6-6.5" stroke="#fff" stroke-width="2.2" fill="none"/></svg>Live Incident Reporting</li>
  <li><svg class="tick" viewBox="0 0 20 20"><circle cx="10" cy="10" r="10" fill="#2196e8"/><path d="M5.5 10.5l3 3 6-6.5" stroke="#fff" stroke-width="2.2" fill="none"/></svg>Automated KPI Tracking</li>
</ul>
<ul class="abs hero-list col-b">
  <li><svg class="tick" viewBox="0 0 20 20"><circle cx="10" cy="10" r="10" fill="#2196e8"/><path d="M5.5 10.5l3 3 6-6.5" stroke="#fff" stroke-width="2.2" fill="none"/></svg>Police Reporting Integration</li>
  <li><svg class="tick" viewBox="0 0 20 20"><circle cx="10" cy="10" r="10" fill="#2196e8"/><path d="M5.5 10.5l3 3 6-6.5" stroke="#fff" stroke-width="2.2" fill="none"/></svg>Smart Scheduling w/payroll</li>
  <li><svg class="tick" viewBox="0 0 20 20"><circle cx="10" cy="10" r="10" fill="#2196e8"/><path d="M5.5 10.5l3 3 6-6.5" stroke="#fff" stroke-width="2.2" fill="none"/></svg>Camera compatibility</li>
</ul>

<!-- features heading -->
<div class="abs section-mark" style="left:580px;top:1132px"></div>
<h2 class="abs heading section-title" style="top:1188px">Our <span class="accent">Features</span></h2>

<!-- feature 1 -->
<div class="abs blob" style="left:-150px;top:1230px;width:500px;height:500px"></div>
<svg class="abs" style="left:68px;top:1341px" width="487" height="352" role="img" aria-label="Photo of an operator watching a wall of monitoring screens">
  <defs><linearGradient id="f1" x1="0" y1="0" x2="1" y2="1"><stop offset="0" stop-color="#3d7ab0"/><stop offset="1" stop-color="#0e2a4a"/></linearGradient></defs>
  <path d="M0 38 Q243 -6 487 38 Q480 210 243 352 Q6 210 0 38Z" fill="url(#f1)"/>
</svg>
<h3 class="abs heading feature-title" style="left:635px;top:1375px">Wardpivot Command<br><span class="accent">Centre</span></h3>
<ul class="abs feature-list" style="left:635px;top:1478px;width:500px">
  <li><svg class="tick" viewBox="0 0 20 20"><circle cx="10" cy="10" r="10" fill="#1a8ad4"/><path d="M5.5 10.5l3 3 6-6.5" stroke="#fff" stroke-width="2.2" fill="none"/></svg><span>Live Incident tracking and reporting with escalation on critical incidents if necessary</span></li>
  <li><svg class="tick" viewBox="0 0 20 20"><circle cx="10" cy="10" r="10" fill="#1a8ad4"/><path d="M5.5 10.5l3 3 6-6.5" stroke="#fff" stroke-width="2.2" fill="none"/></svg><span>Geofence Monitoring to ensure guards at the right location at the right time.</span></li>
  <li><svg class="tick" viewBox="0 0 20 20"><circle cx="10" cy="10" r="10" fill="#1a8ad4"/><path d="M5.5 10.5l3 3 6-6.5" stroke="#fff" stroke-width="2.2" fill="none"/></svg><span>Smart scheduling to ensure the correct training and certifications are assigned to the appropriate guard required.</span></li>
  <li><svg class="tick" viewBox="0 0 20 20"><circle cx="10" cy="10" r="10" fill="#1a8ad4"/><path d="M5.5 10.5l3 3 6-6.5" stroke="#fff" stroke-width="2.2" fill="none"/></svg><span>Camera compatibility to capture live and historical video for incident reporting</span></li>
</ul>

<!-- feature 2 -->
<div class="abs blob" style="left:840px;top:1765px;width:500px;height:500px"></div>
<svg class="abs" style="left:648px;top:1871px" width="484" height="350" role="img" aria-label="Photo of analysts at desks beneath large map and data screens">
  <defs><linearGradient id="f2" x1="0" y1="0" x2="1" y2="1"><stop offset="0" stop-color="#4a8cc4"/><stop offset="1" stop-color="#0f2c4c"/></linearGradient></defs>
  <path d="M0 38 Q242 -6 484 38 Q477 208 242 350 Q6 208 0 38Z" fill="url(#f2)"/>
</svg>
<h3 class="abs heading feature-title" style="left:112px;top:1912px">WardPivot Back Office<br><span class="accent">Administration</span></h3>
<ul class="abs feature-list" style="left:112px;top:2015px;width:510px">
  <li><svg class="tick" viewBox="0 0 20 20"><circle cx="10" cy="10" r="10" fill="#1a8ad4"/><path d="M5.5 10.5l3 3 6-6.5" stroke="#fff" stroke-width="2.2" fill="none"/></svg><span>Automate Police report filing using data from submitted incidents when required.</span></li>
  <li><svg class="tick" viewBox="0 0 20 20"><circle cx="10" cy="10" r="10" fill="#1a8ad4"/><path d="M5.5 10.5l3 3 6-6.5" stroke="#fff" stroke-width="2.2" fill="none"/></svg><span>Track all required KPIs on a per site basis such as vehicle inspections, patrol tour details, etc</span></li>
  <li><svg class="tick" viewBox="0 0 20 20"><circle cx="10" cy="10" r="10" fill="#1a8ad4"/><path d="M5.5 10.5l3 3 6-6.5" stroke="#fff" stroke-width="2.2" fill="none"/></svg><span>Payroll and Invoicing using smart shift reports</span></li>
  <li><svg class="tick" viewBox="0 0 20 20"><circle cx="10" cy="10" r="10" fill="#1a8ad4"/><path d="M5.5 10.5l3 3 6-6.5" stroke="#fff" stroke-width="2.2" fill="none"/></svg><span>Create and manage client sites with configurable geofencing</span></li>
</ul>

<!-- feature 3 -->
<div class="abs blob" style="left:-150px;top:2285px;width:500px;height:500px"></div>
<svg class="abs" style="left:68px;top:2390px" width="483" height="348" role="img" aria-label="Photo of a hand holding a smartphone showing a security app">
  <defs><linearGradient id="f3" x1="0" y1="0" x2="1" y2="1"><stop offset="0" stop-color="#6c7f6a"/><stop offset=".5" stop-color="#7d93b3"/><stop offset="1" stop-color="#2a3b52"/></linearGradient></defs>
  <path d="M0 38 Q241 -6 483 38 Q476 206 241 348 Q6 206 0 38Z" fill="url(#f3)"/>
</svg>
<h3 class="abs heading feature-title" style="left:635px;top:2422px">WardPivot <span class="accent">App</span></h3>
<ul class="abs feature-list" style="left:635px;top:2494px;width:500px">
  <li><svg class="tick" viewBox="0 0 20 20"><circle cx="10" cy="10" r="10" fill="#1a8ad4"/><path d="M5.5 10.5l3 3 6-6.5" stroke="#fff" stroke-width="2.2" fill="none"/></svg><span>Guard can see all site details and instructions when logging onto shift</span></li>
  <li><svg class="tick" viewBox="0 0 20 20"><circle cx="10" cy="10" r="10" fill="#1a8ad4"/><path d="M5.5 10.5l3 3 6-6.5" stroke="#fff" stroke-width="2.2" fill="none"/></svg><span>Ability to view all incidents that have occured at that particular site over the last 'x' days. Understand what has been happening and when.</span></li>
  <li><svg class="tick" viewBox="0 0 20 20"><circle cx="10" cy="10" r="10" fill="#1a8ad4"/><path d="M5.5 10.5l3 3 6-6.5" stroke="#fff" stroke-width="2.2" fill="none"/></svg><span>Report incidents with all relevant information including photo and video</span></li>
  <li><svg class="tick" viewBox="0 0 20 20"><circle cx="10" cy="10" r="10" fill="#1a8ad4"/><path d="M5.5 10.5l3 3 6-6.5" stroke="#fff" stroke-width="2.2" fill="none"/></svg><span>Recieve alerts when repeat offences are occuring within a configurable vicinity.</span></li>
</ul>

<!-- call to action -->
<svg class="abs" style="left:0;top:2905px" width="1200" height="735" role="img" aria-label="Photo of operators facing a holographic city security display">
  <defs><linearGradient id="ctaGrad" x1="0" y1="0" x2="0" y2="1"><stop offset="0" stop-color="#1f5a92"/><stop offset=".55" stop-color="#123a68"/><stop offset="1" stop-color="#0c2a4d"/></linearGradient></defs>
  <path d="M0 40 Q600 -30 1200 40 L1200 420 Q880 560 600 729 Q320 560 0 420 Z" fill="url(#ctaGrad)"/>
</svg>
<h2 class="abs heading cta-title">Ready to Revolutionize<br>Your Security Operations?</h2>
<a class="abs btn btn-cta" href="#">GET STARTED TODAY
  <svg width="22" height="22" viewBox="0 0 20 20"><path d="M4 10h11M11 6l4 4-4 4" stroke="#fff" stroke-width="2.2" fill="none"/></svg></a>

<!-- contact -->
<div class="abs section-mark" style="left:775px;top:3740px"></div>
<h2 class="abs heading contact-title">Contact <span class="accent">Us</span></h2>
<svg class="abs" style="left:199px;top:3798px" width="323" height="372" role="img" aria-label="Photo of a security control room with monitors">
  <defs><linearGradient id="cGrad" x1="0" y1="0" x2="1" y2="1"><stop offset="0" stop-color="#2f6e8e"/><stop offset="1" stop-color="#0a2440"/></linearGradient></defs>
  <path d="M0 30 Q161 -10 323 30 Q318 230 161 372 Q5 230 0 30Z" fill="url(#cGrad)"/>
</svg>
<form>
  <div class="abs field" style="left:586px;top:3899px;width:199px;height:39px">First Name:</div>
  <div class="abs field" style="left:803px;top:3899px;width:199px;height:39px">Last Name:</div>
  <div class="abs field" style="left:586px;top:3957px;width:199px;height:39px">Phone:</div>
  <div class="abs field" style="left:803px;top:3957px;width:199px;height:39px">Email:</div>
  <div class="abs field" style="left:586px;top:4015px;width:416px;height:126px;padding-top:20px">Message:</div>
  <a class="abs btn btn-submit" href="#">SUBMIT
    <svg width="20" height="20" viewBox="0 0 20 20"><path d="M4 10h11M11 6l4 4-4 4" stroke="#fff" stroke-width="2.2" fill="none"/></svg></a>
</form>

<!-- footer -->
<svg class="abs" style="left:0;top:4350px" width="1200" height="580" role="img" aria-label="Dark blue background image of a server room">
  <defs><linearGradient id="ftGrad" x1="0" y1="0" x2="0" y2="1"><stop offset="0" stop-color="#1a4a80"/><stop offset="1" stop-color="#0c2a4d"/></linearGradient></defs>
  <path d="M0 160 Q300 60 600 4 Q900 60 1200 160 L1200 580 L0 580 Z" fill="url(#ftGrad)"/>
</svg>
<div class="abs footer-mark"></div>
<div class="abs footer-name">WardPivot</div>

<div class="abs contact-item" style="left:252px;top:4774px">
  <span class="contact-icon"><svg width="16" height="16" viewBox="0 0 16 16"><path d="M3 1l3 3-1.5 2a9 9 0 005.5 5.5L12 10l3 3-2 2C7 15 1 9 1 3z" fill="#fff"/></svg></span>
  <span>CALL US<br>012 555 0148</span>
</div>
<div class="abs contact-item" style="left:499px;top:4774px">
  <span class="contact-icon"><svg width="16" height="12" viewBox="0 0 16 12"><rect x="0" y="0" width="16" height="12" rx="1.5" fill="#fff"/><path d="M1 1l7 6 7-6" stroke="#2196e8" stroke-width="1.5" fill="none"/></svg></span>
  <span>EMAIL US<br>info@wardpivot-example.com</span>
</div>
<div class="abs contact-item" style="left:795px;top:4774px">
  <span class="contact-icon"><svg width="14" height="18" viewBox="0 0 14 18"><path d="M7 0a7 7 0 017 7c0 5-7 11-7 11S0 12 0 7a7 7 0 017-7z" fill="#fff"/><circle cx="7" cy="7" r="2.5" fill="#2196e8"/></svg></span>
  <span>ADDRESS<br>Address line dummy here</span>
</div>

<div class="abs footer-rule"></div>
<nav class="abs footer-links">
  <span style="left:304px">FEATURES</span>
  <span style="left:397px">|</span>
  <span style="left:482px">PRICING</span>
  <span style="left:571px">|</span>
  <span style="left:662px">CONTACT</span>
  <span style="left:755px">|</span>
  <span style="left:875px">REQUEST A DEMO</span>
</nav>

<div class="abs footer-bar"></div>
<p class="abs copyright">© 2025 WardPivot. All rights reserved.</p>
<span class="abs social" style="left:1016px"></span>
<span class="abs social" style="left:1047px"></span>
<span class="abs social" style="left:1078px"></span>
<span class="abs social" style="left:1109px"></span>

</body>
</html>
```